The tide parlor saltwater aquarium store business card

Looking for a serious business card for a saltwater fish and coral store. I want this thing to blow people's minds when they see it. I would like the card to look very professional but I also want people to know what the tide parlor is just by seeing the card. Iam pretty open to anything as long as it's one of a kind.

Industry/Entity Type

Business

Contact Information for Business Card

31857 Dunmore highway Mardenburg pa 17428. Thetideparlor.example. Customerservice@thetideparlor.example. 5558204716

Requirements
Should not have
• Please no child like fish designs

```html
<!DOCTYPE html>
<html lang="en">
<head>
<meta charset="utf-8">
<title>The Tide Parlor — Business Card</title>
<link rel="stylesheet" href="https://fonts.googleapis.com/css2?family=Lato:wght@400;700;900&display=swap">
<style>
  :root {
    --backdrop: #1b1b1c;
    --card-white: #f6f6f6;
    --ink: #111111;
    --ink-soft: #2b2b2b;
    --ocean: #4a93cf;
    --ocean-light: #5aa6dc;
    --ocean-deep: #3f7fba;
    --divider: #9a9a9a;
  }
  * { box-sizing: border-box; margin: 0; padding: 0; }
  html, body {
    width: 1200px;
    height: 864px;
    overflow: hidden;
    background: var(--backdrop);
    font-family: "Lato", Arial, sans-serif;
  }
  .canvas {
    position: relative;
    width: 1200px;
    height: 864px;
    display: flex;
    align-items: center;
    justify-content: center;
    gap: 40px;
  }
  .card {
    position: relative;
    width: 540px;
    height: 309px;
    border-radius: 4px;
    overflow: hidden;
  }

  /* Front */
  .card-front { background: var(--card-white); }
  .edge-tab {
    position: absolute;
    width: 8px;
    background: var(--ocean);
  }
  .edge-tab--left { left: 0; top: 40px; height: 150px; border-radius: 0 6px 6px 0; }
  .edge-tab--right { right: 0; top: 92px; height: 172px; border-radius: 6px 0 0 6px; }
  .divider {
    position: absolute;
    left: 296px;
    top: 72px;
    width: 1px;
    height: 160px;
    background: var(--divider);
  }
  .contact-block {
    position: absolute;
    left: 82px;
    top: 70px;
    color: var(--ink-soft);
  }
  .person-name {
    font-weight: 900;
    font-size: 16px;
    color: var(--ink);
    letter-spacing: 0.2px;
  }
  .person-title {
    font-size: 10.5px;
    color: var(--ocean);
    letter-spacing: 0.6px;
    margin-top: 1px;
  }
  .contact-list {
    list-style: none;
    margin-top: 14px;
  }
  .contact-list li {
    display: flex;
    align-items: center;
    gap: 8px;
    font-size: 11.5px;
    line-height: 17px;
    margin-left: -18px;
  }
  .contact-icon { width: 11px; height: 11px; fill: var(--ink-soft); flex: none; }
  .address {
    margin-top: 4px;
    margin-left: -18px;
    font-size: 11.5px;
    line-height: 14px;
  }
  .brand-front {
    position: absolute;
    left: 296px;
    right: 8px;
    top: 0;
    bottom: 0;
    display: flex;
    align-items: center;
    justify-content: center;
    gap: 10px;
  }
  .brand-dot {
    width: 22px;
    height: 22px;
    border-radius: 50%;
    background: var(--ocean);
  }
  .brand-name {
    font-weight: 900;
    font-size: 26px;
    color: var(--ocean);
    letter-spacing: 0.3px;
  }

  /* Back */
  .card-back {
    background: linear-gradient(135deg, var(--ocean-deep) 0%, var(--ocean-light) 45%, var(--ocean) 100%);
    display: flex;
    align-items: center;
    justify-content: center;
    gap: 12px;
  }
  .card-back .brand-dot { background: #ffffff; width: 26px; height: 26px; }
  .card-back .brand-name { color: #ffffff; font-size: 32px; }
</style>
</head>
<body>
<main class="canvas">
  <section class="card card-front" aria-label="Business card front">
    <span class="edge-tab edge-tab--left"></span>
    <span class="edge-tab edge-tab--right"></span>

    <div class="contact-block">
      <h1 class="person-name">MARCUS HALE</h1>
      <p class="person-title">PRESIDENT</p>
      <ul class="contact-list">
        <li>
          <svg class="contact-icon" viewBox="0 0 24 24" aria-hidden="true"><path d="M6.6 10.8a15.1 15.1 0 0 0 6.6 6.6l2.2-2.2a1 1 0 0 1 1-.25 11.4 11.4 0 0 0 3.6.57 1 1 0 0 1 1 1V20a1 1 0 0 1-1 1A17 17 0 0 1 3 4a1 1 0 0 1 1-1h3.5a1 1 0 0 1 1 1c0 1.25.2 2.45.57 3.57a1 1 0 0 1-.25 1z"/></svg>
          <span>555-820-4716</span>
        </li>
        <li>
          <svg class="contact-icon" viewBox="0 0 24 24" aria-hidden="true"><path d="M2 5h20v14H2z M3.5 6.5 12 13l8.5-6.5" fill="none" stroke="#2b2b2b" stroke-width="2"/><path d="M2 5h20v2l-10 7L2 7z"/></svg>
          <span>Customerservice@thetideparlor.example</span>
        </li>
        <li>
          <svg class="contact-icon" viewBox="0 0 24 24" aria-hidden="true"><circle cx="12" cy="12" r="9.5" fill="none" stroke="#2b2b2b" stroke-width="2"/><path d="M2.5 12h19M12 2.5c3 3 3 16 0 19M12 2.5c-3 3-3 16 0 19" fill="none" stroke="#2b2b2b" stroke-width="1.6"/></svg>
          <span>www.thetideparlor.example</span>
        </li>
      </ul>
      <p class="address">31857 Dunmore highway,<br>Mardenburg pa 17428</p>
    </div>

    <span class="divider"></span>

    <div class="brand-front">
      <span class="brand-dot"></span>
      <span class="brand-name">The Tide Parlor</span>
    </div>
  </section>

  <section class="card card-back" aria-label="Business card back">
    <span class="brand-dot"></span>
    <span class="brand-name">The Tide Parlor</span>
  </section>
</main>
</body>
</html>
```